Brill Insurance Agency - Business Cards

Hello, I am needing new trendy business cards for our Insurance Agency now that I have a new Logo. I have attached our new logo with several color options along with a business card design that I like. I am leaning towards burgundy and blue colors. I have attached our current business card. I have also attached a headshot of our company president, Martin Vale, that you can use if you wish. Thank you so much in advance for all the wonderful designs!!!!

Target Market(s)

We want to look very professional to potential customers and we also want to look very professional so insurance companies will want to contract with us to sell their product.

Industry/Entity Type

Insurance

Contact Information for Business Card

Martin Vale
mvale@brillagency.com
Business: 555-213-4087
Fax: 555-213-7751
Cell: 555-390-2618
Toll Free: 888-555-0194
42 W Elm Rd Butler, MO 64730
www.brillagency.net

Font styles to use
Serif
Sans Serif

Colors
0355a3
3277b5
f04a50
ec1f27

Requirements
Nice to have
• I love creativity. The more creative and balanced a business card design the more I will like it. I would like the card to be printed horizontally instead of vertically.
Should not have
• My project should not have the Allied Coverage Network logo. It is no longer used in the industry.

```html
<!DOCTYPE html>
<html lang="en">
<head>
<meta charset="utf-8">
<title>Brill Insurance Agency – Business Cards</title>
<link rel="stylesheet" href="https://fonts.googleapis.com/css2?family=Open+Sans:wght@400;600;700&display=swap">
<style>
  :root {
    --brand-blue: #1b5886;
    --accent-red: #e41e26;
    --paper: #ffffff;
    --page: #ffffff;
  }
  * { margin: 0; padding: 0; box-sizing: border-box; }
  html, body { width: 1200px; height: 1003px; overflow: hidden; background: var(--page); }
  body { position: relative; font-family: "Open Sans", Arial, sans-serif; color: var(--brand-blue); }

  .card { position: absolute; left: 341px; width: 518px; height: 296px; }
  .card-front { top: 122px; }
  .card-back { top: 538px; }
  .card-shape { position: absolute; inset: 0; }
  .layer { position: absolute; }

  .brand-mark { width: 40px; height: 40px; border: 4px solid currentColor; border-radius: 50%; }
  .brand-name { font-weight: 700; text-align: center; line-height: 1.15; white-space: nowrap; }
  .brand-name .sub { display: block; letter-spacing: 3px; }

  .front-mark { left: 237px; top: 52px; color: var(--brand-blue); }
  .front-name { left: 0; width: 518px; top: 105px; font-size: 16px; color: var(--brand-blue); }
  .front-name .sub { font-size: 10px; }

  .holder-name { left: 0; width: 518px; top: 170px; text-align: center; color: var(--paper);
    font-size: 20px; font-weight: 700; letter-spacing: 2px; }

  .phone-list { left: 89px; top: 219px; font-size: 8.5px; line-height: 10.5px; color: var(--brand-blue); }
  .phone-list .row { display: flex; }
  .phone-list .label { width: 61px; }
  .web-list { left: 290px; width: 170px; top: 222px; text-align: center; font-size: 9.5px;
    font-weight: 700; line-height: 12px; color: var(--brand-blue); }

  .address { left: 0; width: 518px; top: 279px; text-align: center; font-size: 10px; font-weight: 700; }
  .address .fax-label { color: var(--accent-red); margin-left: 6px; }

  .back-mark { left: 239px; top: 102px; color: var(--paper); }
  .back-name { left: 0; width: 518px; top: 165px; font-size: 20px; color: var(--paper); }
  .back-name .sub { font-size: 12px; }
</style>
</head>
<body>

<section class="card card-front" aria-label="Business card front">
  <svg class="card-shape" width="518" height="296" viewBox="0 0 518 296">
    <rect width="518" height="296" rx="20" fill="var(--brand-blue)"/>
    <path d="M0 40 Q0 19 22 19 H496 Q518 19 518 40 V161 H0 Z" fill="var(--paper)"/>
    <path d="M22 296 Q0 296 0 288 Q0 278 40 278 H478 Q518 278 518 288 Q518 296 496 296 Z" fill="var(--paper)"/>
    <path d="M44 216 H226 L254 234 L226 253 H44 A18.5 18.5 0 0 1 44 216 Z" fill="var(--paper)"/>
    <path d="M474 216 H292 L264 234 L292 253 H474 A18.5 18.5 0 0 0 474 216 Z" fill="var(--paper)"/>
    <circle cx="43" cy="234" r="14" fill="var(--accent-red)"/>
    <path d="M37 228 l3 -1 2 4 -2 2 q2 4 5 5 l2 -2 4 2 -1 3 q-9 1 -13 -13 z" fill="var(--paper)"/>
    <circle cx="474" cy="234" r="14" fill="var(--accent-red)"/>
    <g fill="none" stroke="var(--paper)" stroke-width="1.3">
      <circle cx="474" cy="234" r="7"/>
      <ellipse cx="474" cy="234" rx="3" ry="7"/>
      <path d="M467 234 H481 M468.5 230 H479.5 M468.5 238 H479.5"/>
    </g>
  </svg>

  <div class="layer brand-mark front-mark" aria-hidden="true"></div>
  <div class="layer brand-name front-name">BRILL INSURANCE<span class="sub">AGENCY INC</span></div>

  <div class="layer holder-name">MARTIN VALE</div>

  <div class="layer phone-list">
    <div class="row"><span class="label">Business</span><span>555-213-4087</span></div>
    <div class="row"><span class="label">Call</span><span>555-390-2618</span></div>
    <div class="row"><span class="label">Toll Free</span><span>555-213-7751</span></div>
  </div>
  <div class="layer web-list">
    <div>mvale@brillagency.com</div>
    <div>www.brillagency.net</div>
  </div>

  <div class="layer address">42 W Elm Rd Linden, IA 50099<span class="fax-label">Fax</span> 888-555-0194</div>
</section>

<section class="card card-back" aria-label="Business card back">
  <svg class="card-shape" width="518" height="296" viewBox="0 0 518 296">
    <rect width="518" height="296" rx="20" fill="var(--brand-blue)"/>
    <path d="M62 0 Q72 20 110 20 H408 Q446 20 456 0 Z" fill="var(--paper)"/>
    <path d="M62 296 Q72 277 110 277 H408 Q446 277 456 296 Z" fill="var(--paper)"/>
  </svg>
  <div class="layer brand-mark back-mark" aria-hidden="true"></div>
  <div class="layer brand-name back-name">BRILL INSURANCE<span class="sub">AGENCY INC</span></div>
</section>

</body>
</html>
```